IT business looking for Standout Letterhead Design

We need a letterhead design for a company based in Port Alder, ST 00000 called Corvane Systems, Inc. We specialize in IT engineering, installation and technical support pertaining to the department of defense.

We would like to see a design that incorporates the black and gold that matches our company logo.

More information on the company can be found at www.corvane-sys.example

```html
<!DOCTYPE html>
<html lang="en">
<head>
<meta charset="utf-8">
<title>Corvane Systems Letterhead</title>
<link href="https://fonts.googleapis.com/css2?family=PT+Serif:ital,wght@0,400;0,700;1,400&display=swap" rel="stylesheet">
<style>
  :root {
    --backdrop: #d3d3cc;
    --paper: #ffffff;
    --ink: #2a2a2a;
    --ink-soft: #555555;
    --black: #1c1c1c;
    --gold: #d9a21b;
    --watermark-a: #f4f4f2;
    --watermark-b: #fbfbfa;
  }
  * { box-sizing: border-box; margin: 0; padding: 0; }
  html, body { width: 1200px; height: 1000px; overflow: hidden; }
  body {
    background: var(--backdrop);
    font-family: "PT Serif", Georgia, serif;
    color: var(--ink);
    display: flex; align-items: center; justify-content: center;
  }
  .letterhead {
    position: relative;
    width: 640px; height: 905px;
    background: var(--paper);
    box-shadow: 0 6px 24px rgba(0,0,0,.18);
    overflow: hidden;
  }
  .top-band {
    position: absolute; top: 0; left: 0;
    width: 64px; height: 16px;
    background: var(--black);
    border-bottom: 3px solid var(--gold);
  }
  .top-band--right { left: 172px; width: 24px; }
  .brand {
    position: absolute; top: 24px; left: 74px;
    display: flex; flex-direction: column; align-items: center; gap: 4px;
  }
  .brand-dot {
    width: 30px; height: 30px; border-radius: 50%;
    background: var(--gold);
  }
  .brand-name {
    font-size: 15px; letter-spacing: 3px; font-weight: 400;
    color: var(--black);
  }
  .recipient {
    position: absolute; top: 196px; right: 60px;
    font-size: 9px; color: var(--ink-soft); font-style: italic;
  }
  .body-copy {
    position: absolute; top: 226px; left: 230px; width: 300px;
    font-size: 8.5px; line-height: 1.55; color: var(--ink-soft);
  }
  .body-copy p { margin-bottom: 10px; }
  .body-copy .lead { font-weight: 700; color: var(--ink); }
  .sign-off {
    position: absolute; top: 360px; left: 156px;
    display: flex; flex-direction: column; align-items: flex-start;
  }
  .sign-off svg { display: block; }
  .sign-off .role { font-size: 8.5px; color: var(--ink-soft); margin-top: 2px; }
  .watermark {
    position: absolute; left: 250px; top: 600px;
    width: 340px; height: 280px;
    border-radius: 40%;
    background: radial-gradient(ellipse at 50% 50%, var(--watermark-a) 0%, var(--watermark-b) 55%, var(--paper) 75%);
  }
  .contact {
    position: absolute; left: 26px; bottom: 92px;
    font-size: 9px; line-height: 1.45; color: var(--ink);
    font-style: normal;
  }
  .contact .company { font-weight: 700; }
  .bottom-band {
    position: absolute; left: 0; bottom: 0;
    width: 84px; height: 70px;
    background: var(--black);
    border-top: 4px solid var(--gold);
  }
</style>
</head>
<body>
  <main class="letterhead">
    <div class="top-band"></div>
    <div class="top-band top-band--right"></div>
    <div class="brand">
      <span class="brand-dot"></span>
      <span class="brand-name">CORVANE</span>
    </div>

    <div class="recipient">Dana Whitfield, Director</div>

    <section class="body-copy">
      <p><span class="lead">Lorem Ipsum</span> is simply dummy text of the printing and typesetting industry.</p>
      <p>Lorem Ipsum has been the industry's standard dummy text ever since the 1500s, when an unknown printer took a galley of type and scrambled it to make a type specimen book. It has survived not only five centuries, but also the leap into electronic typesetting, remaining essentially unchanged. It was popularised in the 1960s with the release of Letraset sheets containing Lorem Ipsum passages, and more recently with desktop publishing software like Aldus PageMaker including versions of Lorem Ipsum.</p>
      <p>It is a long established fact that a reader will be distracted by the readable content of a page when looking at its layout. The point of using Lorem Ipsum is that it has a more-or-less normal distribution of letters, as opposed to using 'Content here, content here', making it look like readable English. Many desktop publishing packages and web page editors now use Lorem Ipsum as their default model text, and a search for 'lorem ipsum' will uncover many web sites still in their infancy. Various versions have evolved over the years, sometimes by accident, sometimes on purpose.</p>
      <p>The standard chunk of Lorem Ipsum used since the 1500s is reproduced below for those interested. Sections 1.10.32 and 1.10.33 from "de Finibus Bonorum et Malorum" by Cicero are also reproduced in their exact original form, accompanied by English versions from the 1914 translation by H. Rackham.</p>
    </section>

    <div class="sign-off">
      <svg width="60" height="44" viewBox="0 0 60 44" aria-hidden="true">
        <path d="M20 40 C22 28 24 14 26 4 M26 4 C34 6 36 16 28 20 C24 22 30 26 40 24 M12 30 C24 28 40 30 52 28" fill="none" stroke="var(--black)" stroke-width="1.4" stroke-linecap="round"/>
      </svg>
      <span class="role">General Manager</span>
    </div>

    <div class="watermark" role="img" aria-label="Faint oversized brand emblem watermark area"></div>

    <address class="contact">
      <div class="company">Corvane Systems, Inc.</div>
      <div>1200 Harbor Way</div>
      <div>Port Alder, ST 00000</div>
      <div>(555) 014-2290</div>
      <div>info@corvane-sys.example</div>
      <div>www.corvane-sys.example</div>
    </address>
    <div class="bottom-band"></div>
  </main>
</body>
</html>
```